Business card Zottelgarten

Business card is for a self-employed dog trainer with own dog school. Name and logo of the dog school are available. Color specifications as well. The design should be classy and minimalist, but also modern. An already existing idea would be: Front: Only the logo Back: Contact data

Font styles to use
Serif
Sans Serif
Other font styles liked:
• Trajan Pro

Colors
f78f20

Requirements
Must have
• Name: Margit Wendler-Rasch Title: Dipl. Dog Trainer Contain my logo Follow my font and color preferences (see files)

```html
<!DOCTYPE html>
<html lang="de">
<head>
<meta charset="utf-8">
<title>Zottelgarten – Visitenkarte</title>
<link rel="stylesheet" href="https://fonts.googleapis.com/css2?family=Cinzel:wght@400&family=Lato:wght@300;400&display=swap">
<style>
  :root {
    --bg: #e6e6e4;
    --brown: #6e5444;
    --brown-dark: #5c4538;
    --cream: #efe9e2;
    --paper: #fbfbf8;
    --rule: #8a7668;
  }
  * { margin: 0; padding: 0; box-sizing: border-box; }
  html, body { width: 1200px; height: 1021px; overflow: hidden; }
  body { background: var(--bg); position: relative; }

  .card {
    position: absolute;
    width: 600px;
    height: 388px;
    box-shadow: 0 6px 18px rgba(0,0,0,.18);
  }
  .card--front { left: 80px; top: 100px; background: var(--brown); }
  .card--back  { left: 520px; top: 533px; background: var(--paper); }

  .brand {
    position: absolute;
    display: flex;
    flex-direction: column;
    align-items: center;
  }
  .brand__disc { border-radius: 50%; }
  .brand__name {
    font-family: "Cinzel", serif;
    font-weight: 400;
    letter-spacing: .02em;
    line-height: 1;
  }
  .brand__url {
    font-family: "Cinzel", serif;
    letter-spacing: .42em;
    line-height: 1;
  }

  .card--front .brand { left: 0; right: 0; top: 64px; }
  .card--front .brand__disc { width: 140px; height: 140px; background: var(--cream); }
  .card--front .brand__name { margin-top: 26px; font-size: 40px; color: var(--cream); }
  .card--front .brand__url { margin-top: 6px; font-size: 10px; color: var(--cream); }

  .card--back .brand { left: 40px; width: 250px; top: 118px; }
  .card--back .brand__disc { width: 100px; height: 100px; background: var(--brown); }
  .card--back .brand__name { margin-top: 18px; font-size: 27px; color: var(--brown); }
  .card--back .brand__url { margin-top: 5px; font-size: 7.5px; color: var(--brown); }

  .divider {
    position: absolute;
    left: 318px; top: 92px;
    width: 1px; height: 200px;
    background: var(--rule);
  }

  .contact {
    position: absolute;
    left: 344px; top: 92px;
    font-family: "Lato", sans-serif;
    color: var(--brown-dark);
  }
  .contact__name { font-size: 21px; font-weight: 400; line-height: 1.1; }
  .contact__title { font-size: 11px; font-weight: 400; margin-top: 4px; }
  .contact__list { list-style: none; margin-top: 22px; }
  .contact__item {
    display: flex; align-items: center; gap: 8px;
    font-size: 13px; font-weight: 400;
    margin-bottom: 16px;
  }
  .contact__icon { width: 13px; height: 13px; fill: var(--brown-dark); flex: none; }
  .contact__square { width: 11px; height: 11px; background: var(--brown-dark); flex: none; }
</style>
</head>
<body>

<section class="card card--front" aria-label="Vorderseite">
  <div class="brand">
    <div class="brand__disc"></div>
    <div class="brand__name">Zottelgarten</div>
    <div class="brand__url">www.zottelgarten.ch</div>
  </div>
</section>

<section class="card card--back" aria-label="Rückseite">
  <div class="brand">
    <div class="brand__disc"></div>
    <div class="brand__name">Zottelgarten</div>
    <div class="brand__url">www.zottelgarten.ch</div>
  </div>

  <div class="divider"></div>

  <div class="contact">
    <div class="contact__name">Margit Wendler-Rasch</div>
    <div class="contact__title">Dipl. Hundetrainerin</div>
    <ul class="contact__list">
      <li class="contact__item">
        <svg class="contact__icon" viewBox="0 0 16 16" aria-hidden="true">
          <path d="M2 6c0-2 2.5-3 6-3s6 1 6 3v1h-3V5.5H5V7H2z"/>
          <path d="M4 8h8l1.5 5h-11z"/>
        </svg>
        000 000 0000
      </li>
      <li class="contact__item">
        <svg class="contact__icon" viewBox="0 0 16 16" aria-hidden="true">
          <path d="M1 3h14v10H1z M2 4l6 5 6-5" fill="none" stroke="#5c4538" stroke-width="1.4"/>
        </svg>
        hallo@zottelgarten.ch
      </li>
      <li class="contact__item">
        <span class="contact__square"></span>
        /zottelgarten
      </li>
    </ul>
  </div>
</section>

</body>
</html>
```